International Honeymoon Tour Operator needs Business Card

We need to design a business card including our new logo for a new tour operator called Marisol Thorne Getaways. We would like to also include the text 'Personal Tailor-Made Honeymoons for our Guests at a Lower Cost'. Please Include the following details as well; 'Website: www.marisolthornegetaways.co.uk'; 'E-mail: felix@marisolthornegetaways.co.uk'; 'Mobile: 07914263058'. We would like the design to be compatible with the logo and text. The final design should communicate professionalism, modern and ethical.

We want to business card to be double sided.

We would like to be able to easily adjust the e-mail address and contact number in the future for other employees either through you or ourselves.

Target Market(s)

Brides and grooms aged 18-35 predominantly.

Industry/Entity Type

Business

Colors

Designer to choose colors to be used in the design.

Requirements
Must have
• Logo
Requested Text
Double sided
Nice to have
• Additional colour
The wow factor
Should not have
• Images of currency

```html
<!DOCTYPE html>
<html lang="en">
<head>
<meta charset="utf-8">
<title>Marisol Thorne Getaways — Business Card</title>
<link href="https://fonts.googleapis.com/css2?family=Questrial&display=swap" rel="stylesheet">
<style>
  :root {
    --backdrop: #e6e7ea;
    --card: #ffffff;
    --teal: #3f6f63;
    --olive: #62891f;
    --lime: #a9d84c;
    --shadow: rgba(40, 45, 55, 0.18);
  }
  * { box-sizing: border-box; margin: 0; padding: 0; }
  html, body {
    width: 1200px;
    height: 800px;
    overflow: hidden;
    background: var(--backdrop);
    font-family: "Questrial", "Century Gothic", sans-serif;
  }
  .canvas {
    width: 1200px;
    height: 800px;
    display: flex;
    align-items: center;
    justify-content: center;
    gap: 36px;
  }
  .card {
    position: relative;
    width: 546px;
    height: 312px;
    background: var(--card);
    box-shadow: 0 10px 28px var(--shadow);
    overflow: hidden;
  }

  /* Back side: contact details */
  .contact-list {
    position: absolute;
    top: 22px;
    left: 0;
    right: 0;
    text-align: center;
    list-style: none;
  }
  .contact-item + .contact-item { margin-top: 6px; }
  .contact-label {
    display: block;
    font-size: 11px;
    letter-spacing: 0.06em;
    color: var(--teal);
    text-decoration: underline;
    text-underline-offset: 2px;
    text-transform: uppercase;
  }
  .contact-value {
    display: block;
    font-size: 19px;
    letter-spacing: 0.03em;
    color: var(--olive);
    text-transform: uppercase;
    line-height: 1.25;
  }
  .back-illustration {
    position: absolute;
    left: 40px;
    bottom: 18px;
    width: 280px;
    height: 120px;
    border-radius: 60px 60px 20px 20px;
    background: linear-gradient(135deg, var(--teal) 0%, #5d9a6f 55%, var(--lime) 100%);
  }

  /* Front side: brand */
  .front {
    display: flex;
    flex-direction: column;
    align-items: center;
    padding-top: 40px;
  }
  .front-illustration {
    width: 230px;
    height: 96px;
    border-radius: 48px 48px 12px 12px;
    background: linear-gradient(135deg, #6b5a4e 0%, var(--teal) 45%, var(--lime) 100%);
  }
  .brand-name {
    margin-top: 18px;
    font-size: 34px;
    font-weight: 400;
    color: var(--teal);
    letter-spacing: 0.01em;
  }
  .tagline {
    margin-top: 12px;
    font-size: 15px;
    line-height: 1.3;
    color: var(--olive);
    text-align: center;
    text-transform: uppercase;
    letter-spacing: 0.03em;
  }
</style>
</head>
<body>
<main class="canvas">

  <section class="card back" aria-label="Business card, back side">
    <ul class="contact-list">
      <li class="contact-item">
        <span class="contact-label">Website</span>
        <span class="contact-value">www.marisolthornegetaways.co.uk</span>
      </li>
      <li class="contact-item">
        <span class="contact-label">E-mail</span>
        <span class="contact-value">felix@marisolthornegetaways.co.uk</span>
      </li>
      <li class="contact-item">
        <span class="contact-label">Mobile</span>
        <span class="contact-value">07-914-263-058</span>
      </li>
    </ul>
    <div class="back-illustration" role="img" aria-label="Illustration of two green leaf-winged birds touching beaks, with small hearts"></div>
  </section>

  <section class="card front" aria-label="Business card, front side">
    <div class="front-illustration" role="img" aria-label="Illustration of two green leaf-winged birds perched on a brown branch"></div>
    <h1 class="brand-name">Marisol Thorne Getaways</h1>
    <p class="tagline">Personal tailor-made honeymoons<br>for our guests at a lower cost</p>
  </section>

</main>
</body>
</html>
```